Talon Burke Construction LLC

I like to have a business card the is unique, very professional and the it will projected the best first impression of me and my company

Target Market(s)

Remodeling, new constitution

Industry/Entity Type

Business

Font styles to use
Script

Requirements
Must have
• My company name email and phone number
Nice to have
• A logo maybe

```html
<!DOCTYPE html>
<html lang="en">
<head>
<meta charset="UTF-8">
<title>Talon Burke Construction LLC – Business Card</title>
<link rel="stylesheet" href="https://fonts.googleapis.com/css2?family=Source+Sans+3:wght@400;600;700&display=swap">
<style>
  :root {
    --bg-top: #2a2a2a;
    --bg-bottom: #050505;
    --card-white: #ffffff;
    --brand-red: #d40000;
    --name-red: #c40000;
    --text-grey: #444444;
    --red-top: #f20000;
    --red-bottom: #b00000;
    --mark-red: #9c0000;
  }
  * { margin: 0; padding: 0; box-sizing: border-box; }
  html, body { width: 1200px; height: 900px; overflow: hidden; }
  body {
    position: relative;
    background: linear-gradient(to bottom, var(--bg-top), var(--bg-bottom));
    font-family: "Source Sans 3", "Myriad Pro", Arial, sans-serif;
  }
  .card {
    position: absolute;
    top: 306px;
    height: 271px;
    border-radius: 10px;
  }
  .card-front {
    left: 149px;
    width: 439px;
    background: var(--card-white);
  }
  .card-back {
    left: 608px;
    width: 441px;
    background: linear-gradient(to bottom, var(--red-top), var(--red-bottom));
  }
  .brand-name {
    position: absolute;
    left: 37px;
    top: 92px;
    width: 176px;
    display: flex;
    align-items: center;
    gap: 8px;
    color: var(--brand-red);
    font-weight: 700;
    font-size: 21px;
    line-height: 1.1;
  }
  .brand-square {
    flex: none;
    width: 14px;
    height: 14px;
    background: var(--brand-red);
  }
  .contact {
    position: absolute;
    left: 239px;
    top: 70px;
    color: var(--text-grey);
    font-size: 13.5px;
    line-height: 15px;
  }
  .person-name {
    color: var(--name-red);
    font-weight: 700;
    font-size: 15.5px;
    line-height: 17px;
  }
  .person-title { margin-bottom: 11px; }
  .address { margin-bottom: 12px; }
  .contact-line { display: flex; align-items: center; gap: 7px; line-height: 16px; }
  .contact-line svg { width: 9px; height: 9px; flex: none; fill: var(--brand-red); }
  .back-lockup {
    position: absolute;
    left: 0;
    right: 0;
    top: 152px;
    text-align: center;
    color: var(--mark-red);
    font-weight: 700;
  }
  .back-name {
    font-size: 34px;
    letter-spacing: 1px;
    line-height: 40px;
  }
  .back-sub {
    font-size: 13px;
    letter-spacing: 1px;
    line-height: 16px;
    margin-top: 2px;
  }
</style>
</head>
<body>
  <section class="card card-front">
    <div class="brand-name"><span class="brand-square"></span><span>Talon Burke Construction LLC</span></div>
    <div class="contact">
      <div class="person-name">Marcus Delaney</div>
      <div class="person-title">Managing Director</div>
      <div class="address">4821, Cedar Ridge Road<br>Austin, Texas, 78745.</div>
      <div class="contact-line">
        <svg viewBox="0 0 10 10" aria-hidden="true"><path d="M2 0.5 L3.6 2.6 L2.8 3.8 C3.4 5 4.9 6.6 6.2 7.2 L7.4 6.4 L9.5 8 L8.4 9.6 C4.6 9.4 0.6 5.4 0.4 1.6 Z"/></svg>
        <span>512-555 014 862</span>
      </div>
      <div class="contact-line">
        <svg viewBox="0 0 10 10" aria-hidden="true"><path d="M0.5 2 H9.5 V8.5 H0.5 Z M1.2 2.6 L5 5.6 L8.8 2.6" stroke="#fff" stroke-width="0.7"/></svg>
        <span>info@talonburke.com</span>
      </div>
      <div class="contact-line">
        <svg viewBox="0 0 10 10" aria-hidden="true"><circle cx="5" cy="5" r="4.6"/><path d="M3 3 Q5 4 4 6 M6.5 2.5 Q6 5 7.5 6.5" stroke="#fff" stroke-width="0.8" fill="none"/></svg>
        <span>www.talonburkebuild.com</span>
      </div>
    </div>
  </section>

  <section class="card card-back">
    <div class="back-lockup">
      <div class="back-name">TALON BURKE</div>
      <div class="back-sub">CONSTRUCTION LLC</div>
    </div>
  </section>
</body>
</html>
```